Business Card Design/Logo

I require a design/logo for my own Company, Morvix. The Jewellery I make is totally hand crafted. I own a hand Mining Claim out in the gemfields of Queensland and dig up my own stones. I also fossick for Gold Locally so all my Jewellery products are hand dug/cut/created. Quality stones are hand cut by my partner (Faceted) and other stones (Seconds) are either skin polished or recessed into pieces of Solid 925 Silver or Solid 9ct and 18 ct Gold. I make Sets (Collections) or just one-of designs. All the stones come in different colours and I am now starting to use different colour Golds. The final design should radiate professionalism, quality and uniqueness.

Target Market(s)

Many designs will cost a minimum of AU Dollars $2,000

Industry/Entity Type

Business

Contact Information for Business Card

Morvix Creations
Distinct Bench Wrought Native Adornments
0400327986
P.O. Box 418 Ambercrest 4719 Qld
morvixgarnets@mailbrook.net

```html
<!DOCTYPE html>
<html lang="en">
<head>
<meta charset="utf-8">
<title>Morvix Creations – Business Card</title>
<link rel="stylesheet" href="https://fonts.googleapis.com/css2?family=Cinzel:wght@600&family=Questrial&display=swap">
<style>
  :root {
    --page: #8a8a8a;
    --card-black: #0b0b0b;
    --card-charcoal: #2e2e2e;
    --gold: #d9a21c;
    --silver: #b9b9b9;
    --silver-soft: #9c9c9c;
    --white-soft: #e6e6e6;
  }
  * { margin: 0; padding: 0; box-sizing: border-box; }
  html, body { width: 1200px; height: 900px; overflow: hidden; }
  body {
    background: var(--page);
    display: flex;
    align-items: center;
    justify-content: center;
  }
  .business-card {
    position: relative;
    width: 1000px;
    height: 572px;
    background: var(--card-black);
    overflow: hidden;
    box-shadow: 0 14px 40px rgba(0,0,0,0.45);
  }
  .light-streaks {
    position: absolute;
    inset: 0;
    background:
      radial-gradient(ellipse 60% 35% at 30% 70%, rgba(255,255,255,0.16), transparent 70%),
      radial-gradient(ellipse 70% 30% at 60% 40%, rgba(255,255,255,0.10), transparent 70%),
      linear-gradient(160deg, var(--card-charcoal) 0%, var(--card-black) 55%, #1c1c1c 80%, var(--card-black) 100%);
  }
  .monogram-shade {
    position: absolute;
    right: 40px;
    top: 150px;
    width: 250px;
    height: 250px;
    border-radius: 50%;
    background: var(--gold);
    opacity: 0.12;
  }
  .brand-block {
    position: absolute;
    left: 130px;
    top: 56px;
    width: 580px;
    text-align: center;
  }
  .brand-mark {
    display: inline-block;
    width: 40px;
    height: 40px;
    border-radius: 50%;
    background: var(--silver);
    margin-bottom: 12px;
  }
  .brand-name {
    font-family: 'Cinzel', serif;
    font-weight: 600;
    font-size: 40px;
    letter-spacing: 2px;
    color: var(--gold);
    line-height: 1;
    white-space: nowrap;
  }
  .brand-rule {
    height: 2px;
    width: 460px;
    margin: 12px auto 9px;
    background: var(--gold);
    opacity: 0.8;
  }
  .brand-tagline {
    font-family: 'Cinzel', serif;
    font-weight: 600;
    font-size: 14px;
    letter-spacing: 0.4px;
    color: var(--gold);
    white-space: nowrap;
  }
  .holder {
    position: absolute;
    left: 250px;
    top: 252px;
    font-family: 'Questrial', sans-serif;
    white-space: nowrap;
  }
  .holder-name {
    font-size: 36px;
    color: var(--silver);
    letter-spacing: 1px;
    line-height: 1.15;
  }
  .holder-role {
    font-size: 24px;
    color: var(--silver-soft);
    margin-left: 130px;
    line-height: 1.2;
  }
  .contact {
    position: absolute;
    left: 170px;
    top: 378px;
    width: 520px;
    font-family: 'Questrial', sans-serif;
    font-style: normal;
    color: var(--white-soft);
    font-size: 19px;
    line-height: 1.4;
    text-align: center;
    white-space: nowrap;
  }
</style>
</head>
<body>
  <main class="business-card">
    <div class="light-streaks" role="img" aria-label="Soft white light streaks sweeping across a black background"></div>
    <div class="monogram-shade"></div>

    <section class="brand-block">
      <span class="brand-mark"></span>
      <h1 class="brand-name">Morvix Creations</h1>
      <div class="brand-rule"></div>
      <p class="brand-tagline">Distinct Bench Wrought Native Adornments</p>
    </section>

    <section class="holder">
      <p class="holder-name">GENERIC NAME HERE</p>
      <p class="holder-role">Designation</p>
    </section>

    <address class="contact">
      <p>0400327986 P.O. Box 418 Ambercrest 4719 Qld</p>
      <p>morvixgarnets@mailbrook.net</p>
    </address>
  </main>
</body>
</html>
```